Stationary/business card/envelope design for Larkvale Dentalcare

We are located in the foothills of the sierra nevada mountains. We are looking for a beautiful classy modern stationary. We need evelopes and business card design all to flow seamlessly. Envelope design.

Additional office address 4816 Meridian Wy., Suite B, Auburn, CA 95604 Phone: pending Fax: pending.

3 different Drs on each business card:
Helen R. Marsh, DDS
Orla P. Marsh, DDS
Rebecca S. Halvey, DDS

Target Market(s)

Dental patients

Industry/Entity Type

Dental

Contact Information for Business Card

Two sided. See example.

Font styles to use
Sans Serif

Requirements
Must have
• One sided business cards. Need envelope design.
Colors should match existing logo.

Helen R. Marsh, DDS
Orla P. Marsh, DDS
Rebecca S. Halvey, DDS

```html
<!DOCTYPE html>
<html lang="en">
<head>
<meta charset="utf-8">
<title>Larkvale Dentalcare Stationery</title>
<link href="https://fonts.googleapis.com/css2?family=Arimo:wght@400;700&family=Open+Sans:wght@400;600&family=Lobster&family=Schoolbell&display=swap" rel="stylesheet">
<style>
  :root{
    --backdrop:#e3e3e3;
    --paper:#f4f4f4;
    --green:#166c38;
    --blue:#22a7d1;
    --ink:#222;
    --muted:#444;
    --faint-blue:#d9eaf1;
  }
  *{box-sizing:border-box;margin:0;padding:0}
  html,body{width:1200px;height:986px;overflow:hidden}
  body{background:var(--backdrop);position:relative;font-family:"Arimo",Arial,sans-serif;color:var(--ink)}
  .sheet{position:absolute;background:var(--paper);box-shadow:2px 3px 6px rgba(0,0,0,.28);overflow:hidden}
  .brand{position:absolute;display:flex;flex-direction:column;align-items:center}
  .brand-disc{border-radius:50%;background:var(--blue)}
  .brand-name{font-family:"Open Sans",sans-serif;font-weight:600;color:var(--green);white-space:nowrap;margin-top:4px}
  .faint-disc{position:absolute;border-radius:50%;background:var(--faint-blue);opacity:.75}
  .wave{position:absolute;left:0;bottom:0}
  .site-url{position:absolute;color:#fff;font-family:"Open Sans",sans-serif;letter-spacing:1px}

  /* Letterhead */
  .letterhead{left:66px;top:217px;width:489px;height:632px}
  .letterhead .brand{left:30px;top:30px}
  .letterhead .brand-disc{width:62px;height:62px}
  .letterhead .brand-name{font-size:12px}
  .lh-contact{position:absolute;right:39px;top:51px;text-align:right;font-size:7px;line-height:8.7px;color:var(--muted)}
  .lh-contact .gap{margin-top:2px}
  .ico{display:inline-block;width:6px;height:6px;margin-left:2px;vertical-align:-1px}
  .letter{position:absolute;left:40px;top:161px;width:410px;font-size:7.3px;line-height:9.6px}
  .letter p{margin-bottom:9.6px;text-align:justify}
  .letter .salute{font-weight:700;margin:18px 0 19px}
  .letter .closing{margin-top:22px;margin-bottom:10px}
  .signature{font-family:"Schoolbell",cursive;font-size:13px;line-height:16px;margin-bottom:10px}
  .letterhead .faint-disc{left:252px;top:425px;width:215px;height:215px}
  .letterhead .site-url{left:40px;top:611px;font-size:6.5px}

  /* Business card */
  .card{top:116px;width:115px;height:201px;font-family:"Open Sans",sans-serif}
  .card-front{left:601px}
  .card-front .brand{left:6px;top:18px;width:70px}
  .card-front .brand-disc{width:40px;height:40px}
  .card-front .brand-name{font-size:7px}
  .doctor{font-family:"Lobster",cursive;color:var(--green);font-size:7px}
  .card-front .doctor{position:absolute;left:13px;top:114px}
  .specialty{position:absolute;left:13px;top:123px;font-size:4.6px;color:var(--muted)}
  .card-front .details{position:absolute;left:13px;top:141px;font-size:4.4px;line-height:6.7px;color:var(--muted)}
  .details .row-gap{margin-top:3px}
  .mini-ico{display:inline-block;width:4px;height:4px;border-radius:1px;background:var(--blue);margin-right:2px;vertical-align:0}

  .card-back{left:746px;text-align:center}
  .card-back .faint-disc{left:5px;top:35px;width:100px;height:100px;opacity:.55}
  .appt-lead{position:absolute;left:14px;top:27px;width:87px;border-top:.6px solid #777;padding-top:1px;font-size:4.4px;color:var(--muted)}
  .appt-row{position:absolute;left:14px;width:87px;height:6px;font-size:4.4px;color:var(--muted);text-align:left}
  .appt-row .line{position:absolute;left:13px;right:0;bottom:0;border-bottom:.6px solid #777}
  .appt-row .at{position:absolute;left:57px;bottom:.5px}
  .notice{position:absolute;left:0;right:0;top:147px;font-size:4.4px;line-height:6.8px;color:var(--muted)}
  .card-back .doctor{position:absolute;left:0;right:0;top:164px}
  .card-back .details{position:absolute;left:0;right:0;top:177px;font-size:4.4px;line-height:6.8px;color:var(--muted)}

  /* Envelope front */
  .envelope-front{left:591px;top:353px;width:546px;height:237px;font-family:"Open Sans",sans-serif}
  .envelope-front .brand{left:22px;top:20px;width:76px}
  .envelope-front .brand-disc{width:60px;height:60px}
  .envelope-front .brand-name{font-size:10px}
  .env-address{position:absolute;left:22px;top:113px;width:76px;text-align:center;font-size:4.8px;line-height:6.6px;color:var(--muted)}
  .envelope-front .faint-disc{left:318px;top:38px;width:200px;height:200px}
  .envelope-front .site-url{left:32px;top:218px;font-size:6px}

  /* Envelope back */
  .envelope-back{left:591px;top:613px;width:546px;height:237px}
  .flap{position:absolute;left:-2px;top:0;width:550px;height:80px}
  .envelope-back .brand-disc.seal{position:absolute;left:246px;top:15px;width:54px;height:54px}
</style>
</head>
<body>

<!-- Letterhead -->
<section class="sheet letterhead">
  <div class="brand"><div class="brand-disc"></div><div class="brand-name">Larkvale Dentalcare</div></div>
  <address class="lh-contact" style="font-style:normal">
    <div>4816 Meridian Wy., Suite B</div>
    <div>Auburn, CA 95604</div>
    <div class="gap">(530) 412-6083<svg class="ico" viewBox="0 0 10 10"><path d="M2 1l2 2-1 1.5c.6 1.2 1.3 2 2.5 2.5L7 6l2 2-1.5 1.5C4.5 9 1 5.5.5 2.5z" fill="#22a7d1"/></svg></div>
    <div>(530) 412-6091<svg class="ico" viewBox="0 0 10 10"><rect x="2.5" y="1" width="5" height="3" fill="#22a7d1"/><rect x="1" y="4" width="8" height="4" rx="1" fill="#22a7d1"/></svg></div>
    <div>larkvaledentalcare@mail.com<svg class="ico" viewBox="0 0 10 10"><rect x=".5" y="2" width="9" height="6.5" fill="#22a7d1"/><path d="M.8 2.3L5 5.8l4.2-3.5" stroke="#fff" fill="none" stroke-width=".9"/></svg></div>
  </address>

  <div class="faint-disc" role="img" aria-label="Faint brand circle backdrop"></div>

  <article class="letter">
    <p style="margin-bottom:10px">February 28, 2021</p>
    <p style="margin:0;text-align:left">Mr. Peter Vance<br>President<br>Northfield Group<br>220 Cedar Lane, Suite 4<br>Grass Valley, CA 95945</p>
    <p class="salute">Dear Mr. Peter,</p>
    <p>Lorem ipsum dolor sit amet, consectetur adipiscing elit. Integer diam quam, egestas eu ultrices eu, suscipit ac sapien. Phasellus eu dui nisi. Nam et euismod diam, nec lobortis tortor. Donec et diam nulla. Aenean varius tincidunt convallis. Aliquam a tortor at lacus dictum aliquet. Nunc laoreet metus sapien, in scelerisque augue consectetur in.</p>
    <p>Fusce nec justo laoreet, egestas justo sed, aliquet sem. Pellentesque pharetra massa non orci bibendum semper. Pellentesque cursus eu lectus a consectetur. Nunc volutpat suscipit posuere. Vestibulum facilisis vel quam malesuada mattis. Nulla in mattis tellus. Maecenas tristique mauris vitae pharetra tincidunt. In ut ornare risus. Integer molestie vestibulum nisi, semper dapibus mi condimentum eu.</p>
    <p>Nullam sagittis elit libero, id fringilla est tincidunt eget. Donec in ipsum ultricies, consectetur quam vel, facilisis elit. Phasellus tincidunt congue risus vel luctus. Suspendisse ut mollis neque. Donec ornare orci in turpis vestibulum, in ultrices metus scelerisque. Pellentesque mattis mattis nunc, nec tincidunt lacus egestas id. Fusce facilisis sagittis neque sit amet vulputate. Aliquam ut eros lobortis tortor facilisis vehicula. Sed sed luctus leo, at laoreet sapien. Donec placerat adipiscing ligula non euismod. In lobortis pretium nisl id luctus.</p>
    <p>Integer gravida tincidunt nibh, scelerisque tincidunt turpis. Suspendisse potenti. Nunc hendrerit euismod lectus id elementum. Fusce vitae gravida velit, quis eleifend lectus. In imperdiet mauris eu dui viverra sagittis. Donec tempor dui diam, condimentum gravida lacus pretium a. Nullam fringilla augue quis arcu placerat scelerisque. Aliquam nec tincidunt augue, sit amet posuere ipsum.</p>
    <p class="closing">Sincerely Yours,</p>
    <div class="signature">Helen R. Marsh, DDS</div>
    <p style="margin:0;text-align:left">Helen R. Marsh, DDS<br>Family &amp; Cosmetic Dentistry</p>
  </article>

  <svg class="wave" width="489" height="66" viewBox="0 0 489 66">
    <path d="M0 14 C60 -4 110 -2 200 16 C290 34 350 56 420 50 C450 47 475 30 489 0 V66 H0Z" fill="var(--blue)"/>
    <path d="M0 33 C70 14 130 18 220 38 C300 56 360 58 420 54 C455 51 475 42 489 22 V66 H0Z" fill="var(--green)"/>
  </svg>
  <div class="site-url">www.larkvaledentalcare.com</div>
</section>

<!-- Business card front -->
<section class="sheet card card-front">
  <div class="brand"><div class="brand-disc"></div><div class="brand-name">Larkvale Dentalcare</div></div>
  <div class="doctor">Helen R. Marsh, DDS</div>
  <div class="specialty">Family &amp; Cosmetic Dentistry</div>
  <div class="details">
    <div>4816 Meridian Wy., Suite B</div>
    <div>Auburn, CA 95604</div>
    <div class="row-gap"><span class="mini-ico"></span>(530) 412-6083</div>
    <div><span class="mini-ico"></span>(530) 412-6091</div>
    <div><span class="mini-ico"></span>larkvaledentalcare@mail.com</div>
    <div><span class="mini-ico"></span>www.larkvaledentalcare.com</div>
  </div>
  <svg class="wave" width="115" height="201" viewBox="0 0 115 201">
    <path d="M91 0 C80 50 108 110 96 201 H115 V0Z" fill="var(--blue)"/>
    <path d="M100 0 C90 50 114 110 100 201 H115 V0Z" fill="var(--green)"/>
  </svg>
</section>

<!-- Appointment card -->
<section class="sheet card card-back">
  <div class="faint-disc" role="img" aria-label="Faint brand circle backdrop"></div>
  <div class="appt-lead">has an appointment on</div>
  <div class="appt-row" style="top:46px">Mon<span class="line"></span><span class="at">AT</span></div>
  <div class="appt-row" style="top:66px">Tues<span class="line"></span><span class="at">AT</span></div>
  <div class="appt-row" style="top:86px">Wed<span class="line"></span><span class="at">AT</span></div>
  <div class="appt-row" style="top:106px">Thu<span class="line"></span><span class="at">AT</span></div>
  <div class="appt-row" style="top:126px">Fri<span class="line"></span><span class="at">AT</span></div>
  <div class="notice">IF UNABLE TO KEEP APPOINTMENT<br>KINDLY GIVE 24 HOUR NOTICE</div>
  <div class="doctor">Helen R. Marsh, DDS</div>
  <div class="details">
    <div><span class="mini-ico"></span>(530) 412-6083 <span class="mini-ico"></span>(530) 412-6091</div>
    <div><span class="mini-ico"></span>www.larkvaledentalcare.com</div>
  </div>
</section>

<!-- Envelope front -->
<section class="sheet envelope-front">
  <div class="faint-disc" role="img" aria-label="Faint brand circle backdrop"></div>
  <div class="brand"><div class="brand-disc"></div><div class="brand-name">Larkvale Dentalcare</div></div>
  <div class="env-address">4816 Meridian Wy., Suite B<br>Auburn, CA 95604</div>
  <svg class="wave" width="546" height="46" viewBox="0 0 546 46">
    <path d="M0 14 C60 0 130 -2 230 14 C320 28 380 42 440 38 C490 35 520 20 546 0 V46 H0Z" fill="var(--blue)"/>
    <path d="M0 26 C80 12 150 14 250 28 C330 38 390 44 450 40 C495 37 520 30 546 17 V46 H0Z" fill="var(--green)"/>
  </svg>
  <div class="site-url">www.larkvaledentalcare.com</div>
</section>

<!-- Envelope back -->
<section class="sheet envelope-back">
  <svg class="flap" viewBox="0 0 550 80" width="550" height="80">
    <path d="M2 0 L6 66 Q7 80 22 80 H528 Q543 80 544 66 L548 0" fill="none" stroke="#cfcfcf" stroke-width="1"/>
  </svg>
  <div class="brand-disc seal"></div>
</section>

</body>
</html>
```